Business card for a young woman who performs life enhancement activities with people who have developmental disabilities, what used to be called retardation. She wants to focus on the creative part of her work. She has a degree in art and will engage clients in art projects as well as helping them learn to do things like grocery shop, cook meals, set goals, and live independently.

Target Market(s)

Parents, caregivers, guardians, relatives of people with developmental disabilities, meaning they have not developed in their mental capacities.

Industry/Entity Type

Business

Contact Information for Business Card

Bright Path Care Studio, Marisa J. Tolliver, 417 263-9184, marisa@marisatolliver.example, Life enhancement services for people with developmental disabilities. No address.

Font styles to use
Serif

Requirements
Must have
• Marisa wants it to have some indication of the art or creative part of her work with clients. But it must also be businesslike so it appeals to the parents. They have to see her as a professional, but she's compassionate and artsy. She wants just her company name on the front. The other information should be on the back.

```html
<!DOCTYPE html>
<html lang="en">
<head>
<meta charset="utf-8">
<title>Bright Path Care Studio — Business Card</title>
<link href="https://fonts.googleapis.com/css2?family=Cormorant+Garamond:wght@400;500;600&display=swap" rel="stylesheet">
<style>
  :root {
    --canvas-bg: #ece9e4;
    --front-dark: #121212;
    --front-mid: #363636;
    --band-grey: #595959;
    --band-text: #ececec;
    --back-light: #ffffff;
    --back-shade: #e6e6e6;
    --ink: #1f1f1f;
    --ink-soft: #6a6a6a;
    --brand-purple: #9a4fd0;
    --art-gold: #e0a92e;
    --art-coral: #e2607a;
    --art-violet: #8a45cf;
    --photo-warm: #e9c9a8;
    --photo-cool: #7f8a96;
  }
  * { margin: 0; padding: 0; box-sizing: border-box; }
  html, body { width: 1200px; height: 1023px; overflow: hidden; }
  body {
    background: var(--canvas-bg);
    font-family: "Cormorant Garamond", serif;
    position: relative;
  }
  .card {
    position: absolute;
    top: 357px;
    width: 540px;
    height: 310px;
    border-radius: 4px;
    overflow: hidden;
    box-shadow: 0 10px 28px rgba(0,0,0,0.18);
  }
  .art-stripe {
    height: 4px;
    border-radius: 2px;
    background: linear-gradient(90deg, var(--art-gold), var(--art-coral) 50%, var(--art-violet));
  }

  /* Front */
  .card-front {
    left: 40px;
    background: linear-gradient(160deg, var(--front-mid) 0%, var(--front-dark) 70%);
  }
  .front-photo {
    position: absolute;
    right: 0; top: 0;
    width: 215px; height: 100%;
    background: linear-gradient(150deg, var(--photo-warm) 0%, #c9a486 45%, var(--photo-cool) 100%);
  }
  .front-brand {
    position: absolute;
    left: 34px; top: 78px;
    width: 260px;
  }
  .front-brand .brand-name {
    color: var(--brand-purple);
    font-size: 38px;
    font-weight: 600;
    line-height: 1.02;
  }
  .front-brand .art-stripe { width: 150px; margin-top: 14px; }
  .front-band {
    position: absolute;
    left: 0; bottom: 22px;
    width: 325px; height: 62px;
    background: var(--band-grey);
    display: flex;
    flex-direction: column;
    justify-content: center;
    padding-left: 34px;
    color: var(--band-text);
    font-size: 15px;
    font-weight: 500;
    line-height: 1.3;
  }

  /* Back */
  .card-back {
    left: 620px;
    background: linear-gradient(170deg, var(--back-light) 0%, var(--back-shade) 100%);
  }
  .back-brand {
    position: absolute;
    left: 34px; top: 108px;
    width: 200px;
  }
  .back-brand .brand-name {
    color: var(--brand-purple);
    font-size: 32px;
    font-weight: 600;
    line-height: 1.02;
  }
  .back-brand .art-stripe { width: 120px; margin-top: 12px; }
  .back-divider {
    position: absolute;
    left: 262px; top: 62px;
    width: 1px; height: 186px;
    background: var(--ink);
  }
  .contact {
    position: absolute;
    left: 286px; top: 118px;
  }
  .contact-name {
    font-size: 23px;
    font-weight: 600;
    color: var(--ink);
    letter-spacing: 0.6px;
    margin-bottom: 12px;
  }
  .contact-line {
    display: flex;
    align-items: center;
    gap: 8px;
    font-size: 15px;
    font-weight: 500;
    color: var(--ink);
    margin-bottom: 7px;
  }
  .contact-icon { width: 15px; height: 15px; flex: none; }
</style>
</head>
<body>
  <section class="card card-front">
    <div class="front-photo" role="img" aria-label="Photo of a caregiver and a client smiling together"></div>
    <div class="front-brand">
      <div class="brand-name">Bright Path Care Studio</div>
      <div class="art-stripe"></div>
    </div>
    <div class="front-band">
      <span>Life enhancement services</span>
      <span>for people with developmental disabilities</span>
    </div>
  </section>

  <section class="card card-back">
    <div class="back-brand">
      <div class="brand-name">Bright Path Care Studio</div>
      <div class="art-stripe"></div>
    </div>
    <div class="back-divider"></div>
    <div class="contact">
      <div class="contact-name">MARISA J. TOLLIVER</div>
      <div class="contact-line">
        <svg class="contact-icon" viewBox="0 0 16 16" aria-hidden="true">
          <circle cx="8" cy="8" r="8" fill="var(--brand-purple)"/>
          <path d="M5.2 4.2c.4-.3.8-.2 1 .2l.7 1.3c.2.3.1.7-.2.9l-.5.4c.4.9 1.1 1.6 2 2l.4-.5c.2-.3.6-.4.9-.2l1.3.7c.4.2.5.6.2 1-.6.9-1.4 1.2-2.3.8-1.9-.8-3.2-2.1-4-4-.3-.9 0-1.7.5-2.6z" fill="#fff"/>
        </svg>
        <span>417 263-9184</span>
      </div>
      <div class="contact-line">
        <svg class="contact-icon" viewBox="0 0 16 16" aria-hidden="true">
          <circle cx="8" cy="8" r="8" fill="var(--brand-purple)"/>
          <rect x="4" y="5.2" width="8" height="5.6" rx="0.6" fill="none" stroke="#fff" stroke-width="1"/>
          <polyline points="4.3,5.6 8,8.4 11.7,5.6" fill="none" stroke="#fff" stroke-width="1"/>
        </svg>
        <span>marisa@marisatolliver.example</span>
      </div>
    </div>
  </section>
</body>
</html>
```